Business Cards for a Junk Removal Company

Hello,
We are looking to have business cards designed that are simple, bold, easy to read, and right to the point. Please see the attachments for our logo files. We want the card to be yellow on both sides ( Color code Yellow: #FFE01B). The logo text font is (Rockstar Extra Bold) and this is also in the files attached. Please make the text black for the logo. On the back side of the card, you can use white and black for text. Thank you in advance for your hard work!

Front of card-
Harbor Haul Removal (logo)
Back of card-
Harbor Haul Removal
Donate - Recycle - Dispose
518-276-9053
www.harborhaulremoval.example
info@harborhaulremoval.example

Industry/Entity Type

Junk removal

Contact Information for Business Card

FRONT OF CARD- Harbor Haul Removal (logo) BACK OF CARD- Harbor Haul Removal Donate - Recycle - Dispose 518-276-9053 www.harborhaulremoval.example info@harborhaulremoval.example

Font styles to use
Other font styles liked:
• Rockstar Extra Bold

Colors
FFF300
FFF600
FEFA6F
FFFEC7
FFFEE8

Requirements
Must have
• Must have color code Yellow: #FFE01B for the background of front and back of the card

```html
<!DOCTYPE html>
<html lang="en">
<head>
<meta charset="utf-8">
<title>Harbor Haul Removal — Business Cards</title>
<link href="https://fonts.googleapis.com/css2?family=Oswald:wght@700&display=swap" rel="stylesheet">
<style>
  :root {
    --backdrop: #2a2a2a;
    --card-yellow: #e3c641;
    --card-yellow-deep: #d6b93a;
    --ink: #151512;
    --band-dark: #1a1a16;
  }
  * { margin: 0; padding: 0; box-sizing: border-box; }
  html, body {
    width: 1200px; height: 1138px; overflow: hidden;
    background: var(--backdrop);
    font-family: "Oswald", "Arial Narrow", sans-serif;
    font-weight: 700;
    color: var(--ink);
  }
  .card {
    position: absolute;
    width: 620px; height: 375px;
    border-radius: 14px;
    overflow: hidden;
    background: linear-gradient(160deg, var(--card-yellow) 0%, var(--card-yellow-deep) 100%);
  }
  .card-front { left: 274px; top: 186px; }
  .card-back  { left: 276px; top: 608px; }

  .front-logo {
    position: absolute; left: 0; right: 0; top: 104px;
    text-align: center; text-transform: uppercase; line-height: 1;
  }
  .front-logo .name-main { display: block; font-size: 84px; letter-spacing: -1px; }
  .front-logo .name-sub  { display: block; font-size: 40px; letter-spacing: 10px; margin-top: 12px; padding-left: 10px; }

  .top-band {
    position: absolute; left: 0; top: 0;
    width: 620px; height: 100px;
    background: var(--band-dark);
  }

  .tagline {
    position: absolute; right: 34px; top: 28px;
    text-align: right; text-transform: uppercase;
    color: var(--card-yellow); font-size: 18px; line-height: 26px;
  }

  .back-logo {
    position: absolute; left: 32px; top: 134px;
    text-transform: uppercase; line-height: 1;
  }
  .back-logo .name-main { display: block; font-size: 60px; letter-spacing: -1px; }
  .back-logo .name-sub  { display: block; font-size: 30px; letter-spacing: 8px; margin-top: 8px; }

  .contact-list {
    position: absolute; left: 32px; top: 294px;
    list-style: none; font-size: 15px; text-transform: uppercase;
  }
  .contact-list li { display: flex; align-items: center; gap: 12px; height: 24px; }
  .contact-list svg { width: 16px; height: 14px; }

  .call-block {
    position: absolute; right: 30px; top: 280px;
    text-align: right; text-transform: uppercase; line-height: 1;
  }
  .call-label { display: block; font-size: 18px; }
  .call-number { display: block; font-size: 29px; margin-top: 8px; letter-spacing: 0.5px; }
</style>
</head>
<body>

<section class="card card-front" aria-label="Card front">
  <div class="front-logo">
    <span class="name-main">Harbor Haul</span>
    <span class="name-sub">Removal</span>
  </div>
</section>

<section class="card card-back" aria-label="Card back">
  <div class="top-band" role="img" aria-label="Dark decorative header band"></div>

  <p class="tagline">Donate - Recycle<br>Dispose</p>

  <div class="back-logo">
    <span class="name-main">Harbor Haul</span>
    <span class="name-sub">Removal</span>
  </div>

  <ul class="contact-list">
    <li>
      <svg viewBox="0 0 16 14" aria-hidden="true"><rect x="1" y="2" width="14" height="10" fill="none" stroke="var(--ink)" stroke-width="1.6"/><path d="M1 2 L8 8 L15 2" fill="none" stroke="var(--ink)" stroke-width="1.6"/></svg>
      <span>info@harborhaulremoval.example</span>
    </li>
    <li>
      <svg viewBox="0 0 16 14" aria-hidden="true"><circle cx="8" cy="7" r="6" fill="none" stroke="var(--ink)" stroke-width="1.5"/><ellipse cx="8" cy="7" rx="2.5" ry="6" fill="none" stroke="var(--ink)" stroke-width="1.2"/><line x1="2" y1="7" x2="14" y2="7" stroke="var(--ink)" stroke-width="1.2"/></svg>
      <span>www.harborhaulremoval.example</span>
    </li>
  </ul>

  <div class="call-block">
    <span class="call-label">Call us anytime:</span>
    <span class="call-number">518-276-9053</span>
  </div>
</section>

</body>
</html>
```